I work in the manufacturing industry and currently for TK in the wind department. I'm a contractor. So no TK symbol can be on the card but I can put a wind turbine on it. I am a skydiver as well, so I want a skydiver in the parachute floating next to a turbine with some clouds, the sun over head and the ground below. Hits the moto.

Quality inspection and manufacturing is the industry I work in.

Industry

Harold Tavisky
MQI (manufacturing Quality Inspector)
"Analyzing Quality from a different angle!"

Lumo48213@mailvista.net
555-382-1974

Must have
• Skydiver in parachute, wind turbine, clouds, the sun and the ground. If you can come up with a better moto, please let me know. The back side display "CobleFen inc" in small text in a corner.

```html
<!DOCTYPE html>
<html lang="en">
<head>
<meta charset="utf-8">
<title>Harold Tavisky – Business Card</title>
<link rel="stylesheet" href="https://fonts.googleapis.com/css2?family=Jost:wght@400;700&display=swap">
<style>
  :root {
    --page-bg: #e9e9e9;
    --card-bg: #fbfbfb;
    --ink: #111111;
    --ink-soft: #444444;
    --art-dark: #2a2a2a;
    --art-light: #9a9a9a;
    --card-shadow: rgba(0, 0, 0, 0.18);
  }
  * { margin: 0; padding: 0; box-sizing: border-box; }
  html, body {
    width: 828px;
    height: 1200px;
    overflow: hidden;
    background: var(--page-bg);
    font-family: "Jost", "Futura", sans-serif;
    color: var(--ink);
  }
  .sheet {
    width: 828px;
    height: 1200px;
    display: flex;
    flex-direction: column;
    justify-content: space-evenly;
    align-items: center;
  }
  .card {
    position: relative;
    width: 630px;
    height: 360px;
    background: var(--card-bg);
    box-shadow: 0 6px 18px var(--card-shadow);
  }
  .card-front .artwork {
    position: absolute;
    left: 44px;
    top: 34px;
    width: 250px;
    height: 292px;
    background: linear-gradient(180deg, var(--art-light) 0%, var(--art-dark) 100%);
    opacity: 0.85;
  }
  .card-front .contact {
    position: absolute;
    right: 40px;
    top: 160px;
    text-align: right;
    line-height: 1.3;
    white-space: nowrap;
  }
  .contact .name {
    font-size: 23px;
    font-weight: 700;
  }
  .contact .title {
    font-size: 15px;
    font-weight: 400;
  }
  .contact .email,
  .contact .phone {
    font-size: 20px;
    font-weight: 400;
  }
  .card-back {
    display: flex;
    align-items: center;
    justify-content: center;
  }
  .card-back .motto {
    font-size: 24px;
    font-weight: 400;
    letter-spacing: 0.2px;
    white-space: nowrap;
  }
  .card-back .company {
    position: absolute;
    right: 22px;
    bottom: 16px;
    font-size: 11px;
    font-weight: 400;
    color: var(--ink-soft);
    letter-spacing: 0.4px;
  }
</style>
</head>
<body>
  <main class="sheet">
    <section class="card card-front">
      <div class="artwork" role="img" aria-label="Illustration of a skydiver under a parachute beside a wind turbine, with clouds and the sun overhead"></div>
      <div class="contact">
        <p class="name">Harold Tavisky</p>
        <p class="title">MQI (Manufacturing Quality Inspector)</p>
        <p class="email">Lumo48213@mailvista.net</p>
        <p class="phone">555-382-1974</p>
      </div>
    </section>
    <section class="card card-back">
      <p class="motto">"Analyzing Quality from a different angle!"</p>
      <p class="company">CobleFen inc</p>
    </section>
  </main>
</body>
</html>
```